Kelvar Systems Website

Website design for our company: Kelvar Systems.
The website should look fresh and IT focused. Please have a look at http://www.kelvarsystems.net.au/ for our current design. We want something fresh and new, professional looking, in WordPress so we can easily make changes.

Industry/Entity Type

It Company

```html
<!DOCTYPE html>
<html lang="en">
<head>
<meta charset="utf-8">
<title>Kelvar Systems — Computer and IT Services</title>
<link href="https://fonts.googleapis.com/css2?family=Open+Sans:wght@400;600;700&family=Oxygen:wght@400;700&display=swap" rel="stylesheet">
<style>
:root{
  --green:#00b466;
  --green-dark:#00964f;
  --nav-top:#0a7a45;
  --nav-bottom:#04452a;
  --heading-green:#0b5a2c;
  --accent-green:#0aa350;
  --link-blue:#2d7fb8;
  --text:#555;
  --text-dark:#333;
  --border:#d6d6d6;
  --footer-bg:#f3f3f3;
}
*{margin:0;padding:0;box-sizing:border-box}
html,body{width:914px;height:1200px;overflow:hidden;background:#fff}
body{position:relative;font-family:"Open Sans",Arial,sans-serif;color:var(--text)}
.abs{position:absolute}

.site-header{left:0;top:0;width:914px;height:134px;background:linear-gradient(#00ba6a,#00a95c)}
.brand{left:75px;top:18px;width:131px;height:66px;display:flex;align-items:center;gap:8px}
.brand-dot{width:22px;height:22px;border-radius:50%;background:#fff}
.brand-name{font-family:"Oxygen",sans-serif;font-weight:700;font-size:17px;color:#fff;line-height:1.1}
.phone-support{right:78px;top:41px;text-align:right;color:#fff;font-family:"Oxygen",sans-serif}
.phone-support .label{font-size:13px;opacity:.95}
.phone-support .number{font-size:18px;margin-top:1px}

.main-nav{left:75px;top:95px;width:765px;height:39px;display:flex;background:linear-gradient(var(--nav-top),var(--nav-bottom))}
.main-nav a{display:flex;align-items:center;justify-content:center;color:#fff;text-decoration:none;font-weight:700;font-size:11.5px;border-right:1px solid rgba(255,255,255,.18)}
.main-nav a:last-child{border-right:none}

.hero{left:75px;top:135px;width:765px;height:306px;border:1px solid var(--border);background:#fff;overflow:hidden}
.hero-photo{position:absolute;left:270px;top:0;width:495px;height:306px;background:linear-gradient(90deg,#fff 0%,#e6edf2 18%,#b9c7d3 45%,#6e7a86 75%,#2b2f35 100%)}
.hero-copy{position:absolute;left:46px;top:93px;width:360px;font-family:"Oxygen",sans-serif}
.hero-copy h1{font-weight:400;font-size:29px;color:var(--heading-green);line-height:1.15}
.hero-copy h2{font-weight:400;font-size:24px;color:var(--accent-green);line-height:1.25}
.hero-copy p{font-family:"Open Sans",sans-serif;font-size:10.5px;line-height:17px;margin-top:9px;width:310px}
.dots{display:flex;gap:3px;margin-top:9px}
.dots span{width:11px;height:11px;border-radius:50%;background:#c6c6c6}

.service{top:458px;width:185px}
.service .thumb{width:100%;height:84px}
.service h3{font-family:"Oxygen",sans-serif;font-weight:400;font-size:15px;color:var(--link-blue);margin-top:9px}
.service p{font-size:10px;line-height:16.5px;margin-top:2px}
.service .more{font-size:10.5px;color:var(--text-dark);margin-top:1px;display:block}

.welcome{left:75px;top:692px;width:520px}
.welcome h2{font-family:"Oxygen",sans-serif;font-weight:400;font-size:21px;color:var(--accent-green)}
.welcome .lead{font-size:11.5px;line-height:16.5px;margin-top:11px}
.welcome p{font-size:9.5px;line-height:16.5px;margin-top:7px}

.contact-form{left:647px;top:678px;width:193px;height:205px;border:1px solid var(--border);background:#fff}
.contact-form h3{font-family:"Oxygen",sans-serif;font-weight:400;font-size:16px;color:var(--text-dark);padding:10px 18px 8px;border-bottom:1px solid #e2e2e2;background:linear-gradient(#fff,#f6f6f6)}
.field{margin:6px 0 0 18px;width:159px;height:22px;border:1px solid #cfcfcf;border-radius:2px;font-size:9px;color:#666;padding:5px 9px}
.field:first-of-type{margin-top:12px}
.submit{margin:7px 0 0 18px;width:74px;height:24px;background:linear-gradient(#0ab05a,#038a43);color:#fff;font-weight:600;font-size:11px;display:flex;align-items:center;justify-content:center;border-radius:2px}

.footer-links{left:0;top:933px;width:914px;height:211px;background:var(--footer-bg);border-top:1px solid #ddd}
.footer-col{position:absolute;top:32px}
.footer-col h4{font-family:"Oxygen",sans-serif;font-weight:400;font-size:14px;color:var(--text-dark);margin-bottom:8px}
.footer-col li{list-style:none;font-size:10px;color:var(--text-dark);line-height:18.7px;padding-left:2px}

.footer-bottom{left:0;top:1145px;width:914px;height:55px;border-top:1px solid #e2e2e2;background:#fff}
.copyright{position:absolute;left:71px;top:18px;font-size:9.5px;color:var(--text-dark)}
.social{position:absolute;left:743px;top:17px;display:flex;gap:6px}
.social span{width:16px;height:16px;border-radius:2px}
</style>
</head>
<body>

<header class="abs site-header">
  <div class="abs brand"><span class="brand-dot"></span><span class="brand-name">Kelvar Systems</span></div>
  <div class="abs phone-support"><div class="label">Phone Support</div><div class="number">1300.555.271</div></div>
</header>

<nav class="abs main-nav">
  <a href="#" style="width:83px">HOME</a>
  <a href="#" style="width:110px">ABOUT US</a>
  <a href="#" style="width:95px">CLIENTS</a>
  <a href="#" style="width:103px">SERVICES</a>
  <a href="#" style="width:110px">SUPPORTS</a>
  <a href="#" style="width:129px">TESTIMONIALS</a>
  <a href="#" style="width:135px">CONTACT US</a>
</nav>

<section class="abs hero">
  <div class="hero-photo" role="img" aria-label="Photo of a technician repairing a computer server with a screwdriver"></div>
  <div class="hero-copy">
    <h1>Computer and IT Services</h1>
    <h2>Aliquam erat purus cursus</h2>
    <p>Etiam eu urna Sed porta Suspendisse quam leo molestie sed luctus quis feugiat in pede Fusce tellus Sed metus</p>
    <div class="dots"><span></span><span></span><span></span><span></span></div>
  </div>
</section>

<article class="abs service" style="left:74px">
  <div class="thumb" role="img" aria-label="Photo of a support agent with a headset" style="background:linear-gradient(90deg,#8a5a22,#c89048 55%,#a07038)"></div>
  <h3>On-site Service</h3>
  <p>Pellentesque faucibus Ut accumsan ultricies elit Maecenas at justo</p>
  <span class="more">Read More</span>
</article>
<article class="abs service" style="left:266px">
  <div class="thumb" role="img" aria-label="Photo of a remote support operator at a desk" style="background:linear-gradient(90deg,#e4e4e4,#b8bcc4 50%,#5a6068)"></div>
  <h3>Remote Desktop Support</h3>
  <p>Pellentesque faucibus Ut accumsan ultricies elit Maecenas at justo</p>
  <span class="more">Read More</span>
</article>
<article class="abs service" style="left:462px;width:181px">
  <div class="thumb" role="img" aria-label="Photo of engineers in a server room" style="background:linear-gradient(90deg,#50625c,#9aa8a0 45%,#3e8a78)"></div>
  <h3>Medical IT Service</h3>
  <p>Pellentesque faucibus Ut accumsan ultricies elit Maecenas at justo</p>
  <span class="more">Read More</span>
</article>
<article class="abs service" style="left:651px">
  <div class="thumb" role="img" aria-label="Photo of a help desk team at computer screens" style="background:linear-gradient(90deg,#c8d2dc,#eef0f2 50%,#b4b8bc)"></div>
  <h3>Pharmacy IT Service</h3>
  <p>Pellentesque faucibus Ut accumsan ultricies elit Maecenas at justo</p>
  <span class="more">Read More</span>
</article>

<section class="abs welcome">
  <h2>Welcome to Kelvar Systems Mainpage</h2>
  <p class="lead">Kelvar Systems is an Adelaide based company with a single objective - to excel in the support and service of all computer and IT needs.</p>
  <p>We provide a high level of consulting services using the most experienced engineers at a reasonable and fair price. We believe in using a Business Value approach to every aspect of computer consulting to provide our clients with the most cost effective solutions.</p>
  <p>We strongly believe that we are in business with our clients. Each thing we do must be measured against our clients' business objectives. At the end of the day our client's success is our success.</p>
</section>

<aside class="abs contact-form">
  <h3>Fill Contact Form</h3>
  <div class="field">Full Name</div>
  <div class="field">Email address</div>
  <div class="field">Phone no.</div>
  <div class="field">Message</div>
  <div class="submit">SUBMIT</div>
</aside>

<footer class="abs footer-links">
  <div class="footer-col" style="left:80px"><h4>COMPANY</h4><ul><li>About Us</li><li>Services</li><li>Solutions</li><li>Case Studies</li><li>Awards</li></ul></div>
  <div class="footer-col" style="left:224px"><h4>FEATURES</h4><ul><li>Sed porta</li><li>Suspendisse quam</li><li>Leo molestie</li><li>Sed luctus quis</li><li>Tempor cursus</li></ul></div>
  <div class="footer-col" style="left:381px"><h4>SERVICES</h4><ul><li>Phasellus felis dolor</li><li>Scelerisque tempus</li><li>Eget lobortis</li><li>Libero Aliquam</li></ul></div>
  <div class="footer-col" style="left:539px"><h4>SUPPORT</h4><ul><li>Sed porta</li><li>Suspendisse quam</li><li>Leo molestie</li><li>Sed luctus quis</li></ul></div>
  <div class="footer-col" style="left:681px"><h4>CONTACT</h4><ul><li>48 Harbour Lane, Suite 210</li><li>Adelaide, SA 5000</li><li>Tel: +61 (08) 7420 1185</li><li>hello@kelvarsystems.net.au</li></ul></div>
</footer>

<div class="abs footer-bottom">
  <div class="copyright">© 2014 Company Name.&nbsp; All right reserved.&nbsp; Term of Use</div>
  <div class="social">
    <span style="background:#3b5a96"></span>
    <span style="background:#3fb3e3"></span>
    <span style="background:#1d6fa6"></span>
    <span style="background:#f58a1f"></span>
  </div>
</div>

</body>
</html>
```